Website design 5 pages + short Video + basic graphic optimization for a luxury Homestay - Resort website

I just need the website design for the main pages and optimised graphic images. The website will be mainly based on the following single-page scroll theme.

https://marquinstudio.com/demo/guesthouse-one-page/
FIGMA Templates https://marquinstudio.com/free-figma-design-files-for-hotel-and-vacation-rentals/
You can use these templates as a starting point but create something unique and luxurious.

Find all graphics files here :
1 https://www.storvanta.com/sc/k7q519wp4t2m8r5/AAHJ_Pwoxe47lu829Gbnczq3e
2 https://www.storvanta.com/sh/qmtrk61hxwedzpa/AAC8VolRUM5X7wGHP2NK4ejsu?dl=0

The following is the output :
1. Create website design ( Output high-quality PSD and JPEG files )
a. Homepage ( Example https://marquinstudio.com/demo/countryside2/ )
b. Blog ( Example https://marquinstudio.com/demo/countryside2/blog-2/ )
c. Packages ….. ( Example xxxxx )
d. Room ( Example https://marquinstudio.com/demo/guesthouse-one-page/accommodation/ravelo/ )
e. About us ( Example xxxxx )
f. Contact with embedded google maps ( Example https://marquinstudio.com/demo/hotelclassic/contact-2/ )

2. Short Video edit – 30 to 50 seconds

3. Optimise graphics for all pages and galleries ready to be used in the website ( Output high-quality JPEG files )

```html
<!DOCTYPE html>
<html lang="en">
<head>
<meta charset="utf-8">
<title>Aspra Vista Resort – Home</title>
<link href="https://fonts.googleapis.com/css2?family=Montserrat:wght@500;600;700&family=Lato:wght@400;700&display=swap" rel="stylesheet">
<style>
  :root{
    --ink:#4a4a4a;
    --ink-soft:#6b6b6b;
    --muted:#9a9a9a;
    --line:#e3e3e3;
    --frame:#dcdcdc;
    --accent:#1f7dc1;
    --white:#ffffff;
    --bar:rgba(40,40,40,.45);
  }
  *{box-sizing:border-box;margin:0;padding:0}
  html,body{width:678px;height:1200px;overflow:hidden;background:var(--white)}
  body{position:relative;font-family:"Lato",Arial,sans-serif;color:var(--ink)}
  .abs{position:absolute}

  /* hero */
  .hero{left:0;top:0;width:678px;height:404px;overflow:hidden}
  .hero-photo{position:absolute;inset:0;
    background:
      radial-gradient(ellipse 60% 50% at 20% 55%,rgba(230,190,130,.75),transparent 70%),
      linear-gradient(180deg,#4e6170 0%,#7b8584 35%,#b0946a 62%,#6e5a45 100%);}
  .hero-photo::after{content:"";position:absolute;inset:0;background:rgba(20,25,30,.18)}
  .topbar{left:114px;top:7px;width:450px;height:14px;font:600 5.3px "Montserrat",sans-serif;color:var(--white);letter-spacing:.2px;border-bottom:1px solid rgba(255,255,255,.35)}
  .weather{left:0;top:1px;display:flex;align-items:center;gap:4px}
  .lang{right:0;top:1px;display:flex;align-items:center;gap:4px}
  .lang .sep{width:1px;height:6px;background:rgba(255,255,255,.5);margin:0 3px}
  .logo{left:0;width:678px;top:32px;text-align:center;font:700 11px "Montserrat",sans-serif;color:var(--white);letter-spacing:.3px}
  .nav{top:59px;font:500 6.4px "Montserrat",sans-serif;color:var(--white);display:flex;gap:14px;letter-spacing:.2px}
  .nav-left{left:114px}
  .nav-right{right:114px}
  .caret{font-size:4px;vertical-align:top;margin-left:2px}
  .hero-title{left:0;width:678px;top:140px;text-align:center;font:700 23px "Montserrat",sans-serif;color:var(--white);letter-spacing:-.3px}
  .hero-sub{left:0;width:678px;top:172px;text-align:center;font:400 7.2px "Lato",sans-serif;color:var(--white)}
  .btn-ghost{border:1.5px solid var(--white);color:var(--white);font:700 8px "Montserrat",sans-serif;display:flex;align-items:center;justify-content:center}
  .explore{left:299px;top:223px;width:80px;height:22px}
  .slider-dots{left:657px;top:159px;display:flex;flex-direction:column;gap:3px}
  .slider-dots span{width:6px;height:6px;border-radius:50%;border:1px solid var(--white)}
  .slider-dots span.on{background:var(--white)}
  .booking{left:0;top:333px;width:678px;height:71px;background:var(--bar)}
  .field{top:25px;height:22px;border:1px solid rgba(255,255,255,.7);color:rgba(255,255,255,.85);font:400 7px "Lato",sans-serif;display:flex;align-items:center;justify-content:space-between;padding:0 7px 0 9px}
  .f-arrive{left:114px;width:98px}
  .f-depart{left:222px;width:99px}
  .f-adults{left:330px;width:76px}
  .f-room{left:416px;width:76px}
  .book-now{left:505px;top:25px;width:59px;height:22px;font-size:7.5px}

  /* testimonial */
  .quote-mark{left:0;width:678px;top:432px;text-align:center}
  .testimonial{left:39px;width:600px;top:458px;text-align:center;font:700 11px/14px "Montserrat",sans-serif;color:var(--ink-soft);white-space:nowrap;letter-spacing:-.1px}
  .cite{left:0;width:678px;top:495px;text-align:center;font:500 5.3px "Montserrat",sans-serif;color:var(--muted);letter-spacing:1.2px}
  .cite-rule{left:329px;top:516px;width:20px;height:1px;background:var(--line)}

  /* feature cards */
  .card{top:535px;height:171px;border:1px solid var(--frame);padding:5px;background:var(--white)}
  .card .photo{width:100%;height:100%;display:flex;align-items:center;justify-content:center}
  .card .btn-ghost{width:75px;height:22px;font-size:7.5px}
  .c1{left:114px;width:141px}
  .c2{left:269px;width:140px}
  .c3{left:424px;width:140px}
  .ph-cliff{background:linear-gradient(160deg,#0f2a4a 0%,#1f3d5c 40%,#c9ccd0 65%,#8f8a84 100%)}
  .ph-bed{background:linear-gradient(170deg,#c9b190 0%,#e6d6bc 40%,#b79a73 75%,#8b6f4e 100%)}
  .ph-terrace{background:linear-gradient(180deg,#1d4fa0 0%,#3b6fbe 40%,#d8dde4 62%,#eef0f2 100%)}

  .section-title{font:700 8.5px "Montserrat",sans-serif;color:var(--ink-soft)}
  .t-blog{left:114px;top:737px}
  .t-offer{left:424px;top:737px}
  .blog-frame{left:114px;top:755px;width:295px;height:172px;border:1px solid var(--frame);padding:5px}
  .ph-bay{width:100%;height:100%;background:linear-gradient(180deg,#27426f 0%,#7a7a9a 25%,#c9908e 35%,#3e4a6d 50%,#1f3560 65%,#2f5fa8 100%)}
  .post-title{left:114px;top:939px;width:300px;font:700 11.2px/13.5px "Montserrat",sans-serif;color:var(--accent);white-space:nowrap}
  .post-meta{left:114px;top:976px;width:295px;font:400 5px "Lato",sans-serif;color:var(--ink-soft);display:flex;justify-content:space-between}
  .post-meta a{color:var(--accent);text-decoration:none}
  .post-body{left:114px;top:990px;width:296px;font:400 7.2px/11.7px "Lato",sans-serif;color:var(--ink)}

  .offer-frame{left:424px;top:755px;width:140px;height:170px;border:1px solid var(--frame);padding:5px}
  .ph-town{width:100%;height:100%;background:linear-gradient(180deg,#8a7560 0%,#a7845a 30%,#6b4a32 60%,#3a2a22 100%);position:relative}
  .offer-text{position:absolute;left:27px;top:38px;font:700 7.3px/9px "Montserrat",sans-serif;color:var(--white)}
  .offer-btn{position:absolute;left:27px;top:69px;width:75px;height:31px;font-size:7.5px;line-height:9px;text-align:center}

  .t-social{left:424px;top:945px}
  .social{left:424px;top:962px;display:flex;gap:1px}
  .social span{width:12px;height:12px;border-radius:50%;background:#c4c4c4}
  .t-news{left:424px;top:993px}
  .news-copy{left:424px;top:1012px;width:140px;font:400 7px/11.5px "Lato",sans-serif;color:var(--ink)}
  .news-input{left:424px;top:1041px;width:140px;height:22px;border:1px solid var(--frame);display:flex;align-items:center;justify-content:space-between;padding:0 7px 0 9px;font:400 6.8px "Lato",sans-serif;color:#b5b5b5}

  /* footer */
  .footer-rule{left:114px;top:1111px;width:450px;height:1px;background:#f0f0f0}
  .footer-nav{top:1148px;display:flex;gap:12px;font:400 5.2px "Lato",sans-serif;color:var(--muted);letter-spacing:.2px}
  .fn-left{left:119px}
  .fn-right{right:120px}
  .credit{left:0;width:678px;top:1178px;text-align:center;font:400 4.8px "Lato",sans-serif;color:var(--accent);letter-spacing:.2px}
</style>
</head>
<body>

<header class="hero abs">
  <div class="hero-photo" role="img" aria-label="Sunset view of a whitewashed windmill and terraces above the sea"></div>

  <div class="topbar abs">
    <div class="weather abs">
      <svg width="7" height="7" viewBox="0 0 10 10" fill="none" stroke="#fff" stroke-width="1"><circle cx="5" cy="5" r="2"/><path d="M5 0v1.5M5 8.5V10M0 5h1.5M8.5 5H10M1.5 1.5l1 1M7.5 7.5l1 1M1.5 8.5l1-1M7.5 2.5l1-1"/></svg>
      <span>MESSARIA, GR 25.110000000000014°C</span>
    </div>
    <div class="lang abs">
      <svg width="6" height="6" viewBox="0 0 10 10"><path d="M2 1v9" stroke="#fff"/><path d="M2 1h7l-2 2.5 2 2.5H2z" fill="#fff"/></svg>
      <span>LANGUAGES</span><span class="sep"></span>
      <svg width="7" height="5" viewBox="0 0 7 5"><rect width="7" height="5" fill="#c43b4a"/></svg>
      <span>ENGLISH</span><span class="caret">▾</span>
    </div>
  </div>

  <div class="logo abs">LOGO</div>

  <nav class="nav nav-left abs"><span>HOME</span><span>HOME 2</span><span>LISTING<span class="caret">▾</span></span><span>SINGLE ROOM</span></nav>
  <nav class="nav nav-right abs"><span>BLOG<span class="caret">▾</span></span><span>BOOKING</span><span>GALLERIES</span><span>CONTACT</span></nav>

  <h1 class="hero-title abs">Live your myth in Greece</h1>
  <p class="hero-sub abs">from only $125 / day.</p>
  <div class="btn-ghost explore abs">explore.</div>

  <div class="slider-dots abs"><span class="on"></span><span></span><span></span></div>

  <form class="booking abs">
    <div class="field f-arrive abs">arrive
      <svg width="8" height="8" viewBox="0 0 10 10" fill="none" stroke="#fff"><rect x="1" y="2" width="8" height="7"/><path d="M1 4.5h8M3 1v2M7 1v2"/></svg></div>
    <div class="field f-depart abs">depart
      <svg width="8" height="8" viewBox="0 0 10 10" fill="none" stroke="#fff"><rect x="1" y="2" width="8" height="7"/><path d="M1 4.5h8M3 1v2M7 1v2"/></svg></div>
    <div class="field f-adults abs">adults
      <svg width="7" height="5" viewBox="0 0 8 5" fill="none" stroke="#fff" stroke-width="1.3"><path d="M1 1l3 3 3-3"/></svg></div>
    <div class="field f-room abs">room
      <svg width="7" height="5" viewBox="0 0 8 5" fill="none" stroke="#fff" stroke-width="1.3"><path d="M1 1l3 3 3-3"/></svg></div>
    <div class="btn-ghost book-now abs">book now</div>
  </form>
</header>

<section>
  <div class="quote-mark abs">
    <svg width="20" height="16" viewBox="0 0 20 16" fill="#d6d6d6"><path d="M0 16V9C0 4 2 1 7 0l1 2C5 3 4 5 4 7h4v9zM11 16V9c0-5 2-8 7-9l1 2c-3 1-4 3-4 5h4v9z"/></svg>
  </div>
  <blockquote class="testimonial abs">The best experience ever. Would recommended it everyone. We got married in<br>Santorini, and stayed at Aspra Vista Resort, and it was a dream come true.</blockquote>
  <div class="cite abs">MAREK OLSEN – TRAVEL MAGAZINE</div>
  <div class="cite-rule abs"></div>
</section>

<section>
  <div class="card c1 abs"><div class="photo ph-cliff" role="img" aria-label="White cliffside terraces over a deep blue bay"><div class="btn-ghost">item title.</div></div></div>
  <div class="card c2 abs"><div class="photo ph-bed" role="img" aria-label="Cave suite with a draped canopy bed"><div class="btn-ghost">item title.</div></div></div>
  <div class="card c3 abs"><div class="photo ph-terrace" role="img" aria-label="White terrace with table and chair under a blue sky"><div class="btn-ghost">item title.</div></div></div>
</section>

<main>
  <h2 class="section-title t-blog abs">our blog</h2>
  <div class="blog-frame abs"><div class="ph-bay" role="img" aria-label="Caldera coastline at dusk over calm blue water"></div></div>
  <h3 class="post-title abs">Santorini: Five reasons to visit the beautiful Greek<br>island</h3>
  <div class="post-meta abs">
    <span>POSTED UNDER &nbsp;<a href="#">ARTICLES</a>, <a href="#">MUST VISIT</a>, <a href="#">SANTORINI</a></span>
    <a href="#">3 COMMENTS</a>
  </div>
  <p class="post-body abs">Lorem ipsum dolor sit amet, consectetur adipisicing elit. Ad assumenda fuga illo laudantium magni sed temporibus. Amet atque aut autem consectetur consequuntur dolorum enim error hic inventore molestiae nisi nostrum numquam optio perspiciatis provident, quae quam quisquam quo similique suscipit veniam veritatis vero. Ab culpa cumque deleniti est explicabo facilis, ipsa itaque magni non officiis placeat provident quidem ratione recusandae reiciendis repellat, repudiandae tempora unde voluptates voluptatibus. Ab aliquid, blanditiis debitis eos eveniet ex incidunt itaque, labore maxime mollitia natus perspiciatis porro provident quidem quis reprehenderit rerum suscipit totam ullam voluptatum.</p>

  <aside>
    <h2 class="section-title t-offer abs">special offer</h2>
    <div class="offer-frame abs">
      <div class="ph-town" role="img" aria-label="Hillside village lit up in the evening">
        <div class="offer-text">Our wedding suite.<br>50% off. May 5th.</div>
        <div class="btn-ghost offer-btn">book<br>now.</div>
      </div>
    </div>

    <h2 class="section-title t-social abs">social</h2>
    <div class="social abs" aria-label="Social links"><span></span><span></span><span></span><span></span></div>

    <h2 class="section-title t-news abs">newsletter</h2>
    <p class="news-copy abs">Get explosive offers straight to your inbox and win a free weekend stay!</p>
    <div class="news-input abs">your email
      <svg width="5" height="7" viewBox="0 0 5 8" fill="none" stroke="#555" stroke-width="1.4"><path d="M1 1l3 3-3 3"/></svg>
    </div>
  </aside>
</main>

<footer>
  <div class="footer-rule abs"></div>
  <nav class="footer-nav fn-left abs"><span>HOME</span><span>HOME 2</span><span>LISTING</span><span>SINGLE ROOM</span></nav>
  <nav class="footer-nav fn-right abs"><span>BLOG</span><span>BOOKING</span><span>GALLERIES</span><span>CONTACT</span></nav>
  <div class="credit abs">HOTEL SITE TEMPLATE BY TESSEL WORKS</div>
</footer>

</body>
</html>
```